Build a fresh, contemporary website for a marriage and funeral celebrant

Hi, I'm a marriage celebrant looking for a great redesign of my website.

The site needs to be bright, friendly and full of love and reflect my personality.
I am earthy, friendly, funky, a bit of a hippy, spiritual, caring, creative, professional. I care about the planet, people and believe that love is the answer.

My main area is weddings, but I also offer funerals. I create meaningful, personal ceremonies for any occasion and present them with warmth, humour and compassion.

My current website is hosted by PLOMA, which I hear is not great with zendor. Initial SEO, white hat and all that jazz must be included with the accepted design.

Please see my current website at www.willowvowrites.com.au
PLEASE DO NOT PHONE. I prefer to communicate through the freelancer portal to keep my email free for client contact.

Copy and images will be uploaded

```html
<!DOCTYPE html>
<html lang="en">
<head>
<meta charset="utf-8">
<title>Willow Vow – Mara Vale Celebrant</title>
<link href="https://fonts.googleapis.com/css2?family=Jura:wght@400;500;600&family=Lobster&display=swap" rel="stylesheet">
<style>
:root{
  --teal:#5ccaa6;
  --aqua:#3dbfd4;
  --pink:#e86a86;
  --coral:#f47c7c;
  --ink:#333;
  --grey:#666;
  --soft:#f3f3f3;
  --dark:#4a4a4a;
  --footer:#3d3d3d;
  --line:#b9a7a7;
}
*{box-sizing:border-box;margin:0;padding:0}
html,body{width:1200px;height:4632px;overflow:hidden}
body{position:relative;font-family:"Jura",sans-serif;color:var(--ink);background:#fff}
.abs{position:absolute}
.btn{position:absolute;display:flex;align-items:center;justify-content:center;background:var(--teal);color:#fff;border-radius:22px;font-size:17px;letter-spacing:1px;font-weight:500}
.btn.ghost{background:#fff;color:var(--aqua)}
.rule{position:absolute;height:2px;background:var(--line)}
.rule::before,.rule::after{content:"";position:absolute;top:-3px;width:8px;height:8px;border-radius:50%;border:2px solid var(--line);background:#fff}
.rule::before{left:-8px}.rule::after{right:-8px}
.heading{position:absolute;font-size:32px;letter-spacing:2px;color:#555;font-weight:400}
.heading em{font-style:normal;color:var(--aqua)}
.ph{position:absolute;border-radius:6px}
.para{position:absolute;font-size:13.5px;line-height:24px;color:var(--grey)}
.site-header{position:absolute;left:0;top:0;width:1200px;height:97px;background:#fff;box-shadow:0 2px 6px rgba(0,0,0,.08)}
.brand{position:absolute;left:95px;top:28px;font-size:30px;font-weight:600;color:var(--pink);display:flex;align-items:center;gap:10px}
.brand i{width:14px;height:14px;border-radius:50%;background:var(--pink);display:block}
.nav{position:absolute;left:296px;top:38px;display:flex;gap:33px;font-size:15px;letter-spacing:1px;color:#444}
.social{position:absolute;top:32px;width:32px;height:32px;border-radius:50%;background:var(--pink)}
.hero{position:absolute;left:0;top:97px;width:1200px;height:520px;background:linear-gradient(90deg,#f8efa2 0%,#f6f0b8 30%,#cfe0a0 55%,#9cc27a 75%,#dcead0 100%)}
.hero-title{position:absolute;left:80px;top:112px;font-family:"Lobster",cursive;font-size:38px;line-height:50px;color:#e6a7c4}
.dots{position:absolute;top:651px;left:567px;display:flex;gap:8px}
.dots span{width:9px;height:9px;border-radius:50%;background:#ccc}
.dots span:first-child{background:#fff;border:2px solid var(--pink)}
.play{position:absolute;border-radius:50%;background:#fff;display:flex;align-items:center;justify-content:center}
.band{position:absolute;left:0;width:1200px;display:flex;align-items:center;color:#fff}
.band .title{position:absolute;font-size:33px;letter-spacing:3px}
.band .num{position:absolute;font-size:35px;letter-spacing:3px}
.phone-ico{position:absolute;width:58px;height:58px;border-radius:50%;background:#fff;display:flex;align-items:center;justify-content:center}
.card{position:absolute;width:500px;height:330px;border-radius:4px}
.card.tint{background:linear-gradient(180deg,#bde58c 0%,#7fd6b6 50%,#54c8dd 100%);color:#fff}
.card.plain{background:#fff;box-shadow:0 0 10px rgba(0,0,0,.08)}
.card .av{position:absolute;left:18px;top:22px;width:120px;height:120px;border-radius:50%;background:linear-gradient(135deg,#8fa4b8,#d7c9b4);border:3px solid #fff}
.card .name{position:absolute;left:0;width:156px;top:160px;text-align:center;font-size:13px}
.card .date{position:absolute;left:0;width:156px;top:182px;text-align:center;font-size:11.5px;color:var(--aqua)}
.card .more{position:absolute;left:0;width:156px;top:210px;text-align:center;font-size:11.5px;color:#888}
.card.tint .date,.card.tint .more{color:#fff}
.card .ct{position:absolute;left:160px;top:22px;font-size:16px;letter-spacing:1px}
.card .cr{position:absolute;left:160px;top:50px;width:310px;height:2px;background:#ccc}
.card.tint .cr{background:#fff}
.card .cb{position:absolute;left:160px;top:66px;width:320px;font-size:11.5px;line-height:18.5px;color:#777}
.card.tint .cb{color:#fff}
.card .cb p{margin-bottom:10px}
.cat{position:absolute;font-size:21px;letter-spacing:1px;display:flex;align-items:center;gap:10px}
.cat i{display:block;width:18px;height:18px;background:var(--aqua);border-radius:3px}
.prov{position:absolute;display:flex;align-items:center;gap:18px;font-size:15px;color:#777;letter-spacing:1px}
.prov b{display:block;width:78px;height:52px;border-radius:3px;box-shadow:0 0 4px rgba(0,0,0,.2);font-weight:400}
.vdiv{position:absolute;width:1px;background:#ddd}
.footer{position:absolute;left:0;top:4258px;width:1200px;height:374px;background:var(--footer);color:#fff}
.fcol h4{font-size:20px;font-weight:500;letter-spacing:1px;margin-bottom:20px}
.fcol{position:absolute;top:50px}
.fcol li{list-style:none;font-size:11.5px;line-height:31px;color:#ddd}
.fsoc{position:absolute;top:226px;width:32px;height:32px;border-radius:50%;border:2px solid #fff}
.copy{position:absolute;left:0;top:336px;width:1200px;height:38px;background:#2e2e2e;text-align:center;font-size:11px;line-height:38px;color:#ccc}
</style>
</head>
<body>

<header class="site-header">
  <div class="brand"><i></i>Willow Vow</div>
  <nav class="nav"><span>Home</span><span>Meet Mara</span><span>Rave Reviews</span><span>Love Love Love</span><span>Say Hi</span><span>Links</span></nav>
  <span class="social" style="left:1042px"></span>
  <span class="social" style="left:1086px"></span>
</header>

<section class="hero">
  <div role="img" aria-label="Photo of a bride and groom embracing outdoors" class="abs" style="left:520px;top:0;width:680px;height:520px;background:radial-gradient(ellipse at 55% 50%,#b9b0a4 0%,#7f9a66 45%,rgba(156,194,122,0) 75%)"></div>
  <h1 class="hero-title">Woo Hoo! You're<br>Getting Married!</h1>
  <p class="abs" style="left:80px;top:233px;font-size:19px;letter-spacing:1px">Congratulations!</p>
  <p class="abs" style="left:80px;top:278px;font-size:15px;line-height:24px;letter-spacing:.5px">You've booked the venue, bought<br>the rings, hired the band...</p>
  <span class="btn" style="left:80px;top:353px;width:150px;height:42px">Let's Do It</span>
</section>
<div class="dots"><span></span><span></span><span></span><span></span></div>

<div role="img" aria-label="Video still of a wedding ceremony in a garden" class="ph" style="left:80px;top:745px;width:398px;height:270px;background:linear-gradient(160deg,#5b6650,#8d8c7c 50%,#4b5a3c)"></div>
<div class="play" style="left:254px;top:855px;width:48px;height:48px"><svg width="20" height="22"><path d="M4 2 L18 11 L4 20Z" fill="#e03b3b"/></svg></div>
<div role="img" aria-label="Video thumbnail" class="ph" style="left:80px;top:1034px;width:85px;height:56px;border:3px solid var(--teal);background:#7b8a6a"></div>
<div role="img" aria-label="Video thumbnail" class="ph" style="left:183px;top:1034px;width:85px;height:56px;border:3px solid var(--teal);background:#6b8fb5"></div>
<div role="img" aria-label="Video thumbnail" class="ph" style="left:287px;top:1034px;width:85px;height:56px;border:3px solid var(--teal);background:#6d5d4f"></div>
<div role="img" aria-label="Video thumbnail" class="ph" style="left:392px;top:1034px;width:85px;height:56px;border:3px solid var(--teal);background:#9aa58a"></div>
<h2 class="heading" style="left:648px;top:740px;font-size:27px">Ready to make <em>some magic?</em></h2>
<div class="rule" style="left:643px;top:782px;width:435px"></div>
<h3 class="abs" style="left:634px;top:840px;font-size:19px;font-weight:500;letter-spacing:1px">Eek! What about the ceremony!</h3>
<p class="para" style="left:634px;top:883px;width:375px">Relax! Together, we can create something magical, something unique to reflect who you are as a couple and what this moment and the rest of your forever means to the two of you.</p>
<span class="btn" style="left:634px;top:1005px;width:126px;height:36px">Let's Do It</span>
<span class="abs" style="left:815px;top:1013px;font-size:14px;color:var(--teal)">View More »</span>

<section class="abs" style="left:0;top:1175px;width:1200px;height:550px;background:linear-gradient(90deg,var(--soft) 60%,#e6f5f7 80%,#aee6f2 100%)"></section>
<h2 class="heading" style="left:110px;top:1228px">Hey there, <em>I'm Mara,</em></h2>
<div class="rule" style="left:85px;top:1282px;width:432px"></div>
<p class="abs" style="left:80px;top:1338px;font-size:19px;line-height:24px;letter-spacing:1px">.....lover of mountains, chocolate and<br>echidnas.</p>
<p class="para" style="left:80px;top:1410px;width:420px">I've been crafting unique ceremonies for amazing people since 2012 and truly love sharing the joy as they mark their most memorable moments in life.</p>
<p class="para" style="left:80px;top:1493px;width:420px">I live on 20 acres near Fernvale in the hill country with my beautiful husband and 3 gloriously happy and cheeky children.</p>
<span class="btn" style="left:80px;top:1600px;width:140px;height:40px;font-size:15px">Let's Talk...</span>
<div role="img" aria-label="Portrait of the celebrant framed among blossoms" class="abs" style="left:705px;top:1266px;width:370px;height:370px;border-radius:50%;background:radial-gradient(circle,#6d6d6d 30%,#b5536a 55%,#e9b9c4 100%)"></div>

<div class="band" style="top:1725px;height:111px;background:linear-gradient(90deg,#f47c7c,#f06f78 60%,#f29a95)">
  <span class="title" style="left:80px">Mara Vale Celebrant</span>
  <span class="phone-ico" style="left:520px"><svg width="28" height="28" viewBox="0 0 24 24"><path d="M6.6 10.8a15 15 0 0 0 6.6 6.6l2.2-2.2a1 1 0 0 1 1-.25 11.4 11.4 0 0 0 3.6.57 1 1 0 0 1 1 1V20a1 1 0 0 1-1 1A17 17 0 0 1 3 4a1 1 0 0 1 1-1h3.5a1 1 0 0 1 1 1c0 1.25.2 2.45.57 3.57a1 1 0 0 1-.25 1z" fill="var(--teal)"/></svg></span>
  <span class="num" style="left:595px">0400 217 964</span>
  <span class="btn ghost" style="left:918px;top:37px;width:142px;height:36px;color:var(--coral);font-size:15px">Let's Do It</span>
</div>

<section class="abs" style="left:0;top:1836px;width:1200px;height:640px;background:linear-gradient(160deg,#eef8e4 0%,#fff 35%,#fff 80%,#fdf3e6 100%)"></section>
<div role="img" aria-label="Wedding photo" class="ph" style="left:80px;top:1975px;width:138px;height:133px;background:#6e5e50"></div>
<div role="img" aria-label="Wedding photo" class="ph" style="left:80px;top:2122px;width:138px;height:133px;background:#7d8a5d"></div>
<div role="img" aria-label="Wedding photo" class="ph" style="left:80px;top:2270px;width:138px;height:133px;background:#56683f"></div>
<div role="img" aria-label="Wedding photo" class="ph" style="left:232px;top:1975px;width:138px;height:133px;background:#5f8fc4"></div>
<div role="img" aria-label="Wedding photo" class="ph" style="left:232px;top:2122px;width:138px;height:133px;background:#8fb0a4"></div>
<div role="img" aria-label="Wedding photo" class="ph" style="left:232px;top:2270px;width:138px;height:185px;background:#6b5a48"></div>
<div role="img" aria-label="Wedding photo" class="ph" style="left:383px;top:1922px;width:139px;height:186px;background:#b99985"></div>
<div role="img" aria-label="Wedding photo" class="ph" style="left:383px;top:2122px;width:139px;height:133px;background:#8ab0c8"></div>
<div role="img" aria-label="Wedding photo" class="ph" style="left:383px;top:2270px;width:139px;height:133px;background:#9ba88a"></div>
<h2 class="heading" style="left:707px;top:1960px">Love, Love <em>Crazy Love!</em></h2>
<div class="rule" style="left:690px;top:2005px;width:430px"></div>
<p class="para" style="left:683px;top:2060px;width:437px">It is a long established fact that a reader will be distracted by the readable content of a page when looking at its layout. The point of using Lorem Ipsum is that it has a more-or-less normal distribution of letters, as opposed to using 'Content here, content here', making it look like readable English.</p>
<p class="para" style="left:683px;top:2202px;width:437px">It is a long established fact that a reader will be distracted by the readable content of a page when looking at its layout. The point of using Lorem Ipsum.</p>
<span class="btn" style="left:683px;top:2316px;width:140px;height:36px;font-size:15px">Let's Talk...</span>

<h2 class="heading" style="left:0;width:1200px;text-align:center;top:2525px">Happy <em>Couples Say...</em></h2>
<div class="rule" style="left:385px;top:2580px;width:430px"></div>

<div class="card tint" style="left:80px;top:2677px;width:498px">
  <div class="av" role="img" aria-label="Couple photo"></div>
  <div class="name">Rosa and Finn</div><div class="date">Sept 6, 2018</div><div class="more">View More ›</div>
  <div class="ct">Best Wedding Ever!</div><div class="cr"></div>
  <div class="cb"><p>We were after a celebrant who was a bit 'left of centre', like we are. We met with Mara and liked her immediately. She was warm, friendly, and fun from the outset. Mara helped us every step of the way with her professional, but caring, offbeat style that I loved.</p><p>She led our ceremony beautifully. The service was just perfect, taking everything we wanted and turning it to a phenomenal and unforgettable experience - more than we could have imagined.</p></div>
</div>
<div class="card plain" style="left:620px;top:2677px;width:510px">
  <div class="av" role="img" aria-label="Couple photo"></div>
  <div class="name">Carla and Nate</div><div class="date">Sept 6, 2018</div><div class="more">View More ›</div>
  <div class="ct">Phenomenal!</div><div class="cr"></div>
  <div class="cb"><p>Our wedding day was perfect, by far the best days of our lives - made even more special by having you perform our ceremony. The service was just perfect, taking everything we wanted and turning it to a phenomenal and unforgettable experience - more than we could have imagined.</p><p>Thank you so much, you are amazing, incredibly professional, caring and calming. I would have no hesitation in recommending your services.</p></div>
</div>
<div class="card plain" style="left:80px;top:3060px;width:498px;box-shadow:none">
  <div class="av" role="img" aria-label="Couple photo"></div>
  <div class="name">Jed and Olivia</div><div class="date">Sept 6, 2018</div><div class="more">View More ›</div>
  <div class="ct">The Most Beautiful Ceremony!</div><div class="cr"></div>
  <div class="cb"><p>The ceremony went off without a hitch. Mara was fabulous! We have been inundated with people saying that it was one of the most beautiful ceremonies they've been to, so we are clearly not alone in our opinion of how good Mara was. She was just brilliant.</p><p>Mara takes great pride in her work, and approached the writing of our ceremony with great care and respect. We felt valued and the day wouldn't have been anywhere near as special without her input. SHE ROCKS!</p></div>
</div>
<div class="card tint" style="left:620px;top:3060px;width:500px">
  <div class="av" role="img" aria-label="Couple photo"></div>
  <div class="name">Tess and Owen</div><div class="date">Sept 6, 2018</div><div class="more">View More ›</div>
  <div class="ct">Just Perfect!</div><div class="cr"></div>
  <div class="cb"><p>Mara was our celebrant for our wedding at Hilltop Rest Retreat on February 4th - and she was perfect!</p><p>Our checklist was for someone easy going, vibrant and contemporary - and Mara hit the mark.</p><p>Our 'story' she put together worked wonderfully and it was a pleasure to communicate with her and we would highly recommend her for any occasion she can officiate. Thanks Mara!</p></div>
</div>

<div class="band" style="top:3472px;height:108px;background:var(--dark)">
  <span class="title" style="left:140px">We Also Do Obituaries</span>
  <span class="phone-ico" style="left:571px"><svg width="28" height="28" viewBox="0 0 24 24"><path d="M6.6 10.8a15 15 0 0 0 6.6 6.6l2.2-2.2a1 1 0 0 1 1-.25 11.4 11.4 0 0 0 3.6.57 1 1 0 0 1 1 1V20a1 1 0 0 1-1 1A17 17 0 0 1 3 4a1 1 0 0 1 1-1h3.5a1 1 0 0 1 1 1c0 1.25.2 2.45.57 3.57a1 1 0 0 1-.25 1z" fill="var(--teal)"/></svg></span>
  <span class="num" style="left:648px">0400 217 964</span>
  <span class="btn ghost" style="left:948px;top:36px;width:142px;height:36px;font-size:15px">Let's Talk...</span>
</div>

<h2 class="heading" style="left:0;width:1200px;text-align:center;top:3638px">Other Amazing <em>Service Providers</em></h2>
<div class="rule" style="left:300px;top:3690px;width:600px"></div>
<p class="abs" style="left:0;width:1200px;text-align:center;top:3738px;font-size:13.5px;color:var(--grey)">The wedding industry is jam packed with incredible people. Here's a few I love and recommend....</p>
<div class="vdiv" style="left:362px;top:3810px;height:250px"></div>
<div class="vdiv" style="left:718px;top:3810px;height:250px"></div>

<div class="cat" style="left:80px;top:3810px"><i></i>Caterers</div>
<div class="rule" style="left:80px;top:3843px;width:205px"></div>
<div class="prov" style="left:82px;top:3862px"><b style="background:#c9302c"></b>Harbour Table Catering</div>
<div class="prov" style="left:82px;top:3942px"><b style="background:#a9a46a"></b>Orchard Plate Catering</div>

<div class="cat" style="left:425px;top:3810px"><i></i>Cakes</div>
<div class="rule" style="left:425px;top:3843px;width:205px"></div>
<div class="prov" style="left:428px;top:3868px"><b style="background:#f1d7a4"></b>Frosted Crumb</div>
<div class="cat" style="left:425px;top:3953px"><i></i>Florists</div>
<div class="rule" style="left:425px;top:3986px;width:205px"></div>
<div class="prov" style="left:428px;top:4005px"><b style="background:#a4653f"></b>Petal Lane Florals</div>

<div class="cat" style="left:782px;top:3810px"><i></i>Photographers</div>
<div class="rule" style="left:782px;top:3843px;width:205px"></div>
<div class="prov" style="left:785px;top:3868px"><b style="background:#2a2a2a"></b>June Harlow Photography</div>
<div class="cat" style="left:782px;top:3953px"><i></i>Jewellers</div>
<div class="rule" style="left:782px;top:3986px;width:205px"></div>
<div class="prov" style="left:785px;top:4005px;line-height:24px"><b style="background:#5a5fae"></b>Northvale Fine<br>Jewellers</div>

<div class="band" style="top:4145px;height:113px;background:linear-gradient(90deg,#4fc6c8,#6fd3c8 50%,#47bfd3)">
  <span class="title" style="left:140px">We Also Do Obituaries</span>
  <span class="phone-ico" style="left:571px"><svg width="28" height="28" viewBox="0 0 24 24"><path d="M6.6 10.8a15 15 0 0 0 6.6 6.6l2.2-2.2a1 1 0 0 1 1-.25 11.4 11.4 0 0 0 3.6.57 1 1 0 0 1 1 1V20a1 1 0 0 1-1 1A17 17 0 0 1 3 4a1 1 0 0 1 1-1h3.5a1 1 0 0 1 1 1c0 1.25.2 2.45.57 3.57a1 1 0 0 1-.25 1z" fill="var(--teal)"/></svg></span>
  <span class="num" style="left:648px">0400 217 964</span>
  <span class="btn ghost" style="left:948px;top:38px;width:142px;height:36px;font-size:15px">Let's Talk...</span>
</div>

<footer class="footer">
  <div class="abs" style="left:158px;top:82px;font-size:34px;font-weight:600;color:var(--pink);display:flex;align-items:center;gap:10px"><span style="width:16px;height:16px;border-radius:50%;background:var(--pink);display:block"></span>Willow Vow</div>
  <span class="fsoc" style="left:156px;background:#fff"></span>
  <span class="fsoc" style="left:200px"></span>
  <span class="fsoc" style="left:244px"></span>
  <span class="fsoc" style="left:288px"></span>
  <div class="fcol" style="left:459px"><h4>Quick Links</h4><ul><li>Home</li><li>Meet Mara</li><li>Rave Review</li><li>Love Love Love</li><li>Contact</li></ul></div>
  <div class="fcol" style="left:691px"><h4>Useful Links</h4><ul><li>Caterers</li><li>Cakes</li><li>Celebrants</li><li>Jewellers</li><li>Photographers</li><li>Venues</li><li>Wedding Planners</li></ul></div>
  <div class="fcol" style="left:893px"><h4>Get In Touch</h4>
    <svg class="abs" style="left:0;top:48px" width="12" height="14" viewBox="0 0 12 14"><path d="M6 14 L6 5 M1 5 L6 0 L11 5" stroke="var(--aqua)" stroke-width="2" fill="none"/></svg>
    <p class="abs" style="left:28px;top:46px;width:220px;font-size:11.5px;line-height:22px;color:#ddd">12 Fernhill Rd, Briarwood,<br>Tasmania , Australia</p>
    <svg class="abs" style="left:0;top:100px" width="12" height="12" viewBox="0 0 24 24"><path d="M6.6 10.8a15 15 0 0 0 6.6 6.6l2.2-2.2a1 1 0 0 1 1-.25 11.4 11.4 0 0 0 3.6.57 1 1 0 0 1 1 1V20a1 1 0 0 1-1 1A17 17 0 0 1 3 4a1 1 0 0 1 1-1h3.5a1 1 0 0 1 1 1c0 1.25.2 2.45.57 3.57a1 1 0 0 1-.25 1z" fill="var(--aqua)"/></svg>
    <p class="abs" style="left:28px;top:96px;width:200px;font-size:11.5px;color:#ddd">0400 217 964</p>
    <svg class="abs" style="left:0;top:140px" width="13" height="10"><rect x="0.5" y="0.5" width="12" height="9" fill="var(--aqua)"/><path d="M0.5 0.5 L6.5 5 L12.5 0.5" stroke="#3d3d3d" fill="none"/></svg>
    <p class="abs" style="left:28px;top:137px;width:260px;font-size:11.5px;color:#ddd">love@willowvowrites.com.au</p>
  </div>
  <div class="copy">© Copyright Mara Vale Celebrant</div>
</footer>

</body>
</html>
```